Business card for Luxury Portable Restroom Trailer company

We are a Luxury Portable Restroom Trailer Company Called PELIKAR HIRES. Based in Orange County California. We provide portable restroom trailers for events, such as, Weddings, Concerts, Charity events, Sporting events, Tournaments, Corporate events, ect. We rent and Sell the Luxury restrooms. Our colors are white, grey, and Orange. As you will see in the logo we uploaded.
There are 2 people in the company so the names and titles will change for the 3 people but card will remain the same. Here is the information for each Person: Dennis Moyle CFO 555 018-3647
next Person: Wesley Tanford VP 555 018-3647
Next Person: Miles Tanford CEO 555 018-3647
Information to include on the card: Luxury Restroom Trailers Rental and Sales. Weddings, Concerts, Charity, Sporting and Corp. Events.

```html
<!DOCTYPE html>
<html lang="en">
<head>
<meta charset="utf-8">
<title>Pelikar Hires – Business Card</title>
<link rel="stylesheet" href="https://fonts.googleapis.com/css2?family=Montserrat:wght@400;500;700&display=swap">
<style>
  :root {
    --backdrop: #cfd3d4;
    --card: #f7f7f6;
    --orange: #d9541e;
    --charcoal: #2f3133;
    --grey: #55585b;
    --faint: #e6e6e5;
  }
  * { box-sizing: border-box; margin: 0; padding: 0; }
  html, body { width: 1200px; height: 829px; overflow: hidden; }
  body {
    background: var(--backdrop);
    font-family: "Montserrat", Arial, sans-serif;
    position: relative;
  }
  .card {
    position: absolute;
    top: 250px;
    width: 540px;
    height: 309px;
    background: var(--card);
    border-bottom: 4px solid var(--orange);
    box-shadow: 0 8px 22px rgba(0,0,0,.18);
    overflow: hidden;
  }
  .card--front { left: 40px; }
  .card--back { left: 620px; }

  .brand {
    position: absolute;
    display: flex;
    align-items: center;
    gap: 10px;
    font-weight: 700;
    color: var(--orange);
    letter-spacing: 1px;
    white-space: nowrap;
  }
  .brand__mark { background: var(--orange); display: block; }

  .card--front .brand { left: 34px; top: 34px; font-size: 26px; }
  .card--front .brand__mark { width: 14px; height: 14px; }

  .address {
    position: absolute; left: 34px; top: 100px;
    font-size: 12.5px; line-height: 1.45; color: var(--grey);
  }
  .contacts {
    position: absolute; left: 34px; top: 152px;
    list-style: none; font-size: 12.5px; line-height: 1.8; color: var(--grey);
  }
  .contacts li { display: flex; align-items: center; gap: 8px; }
  .contacts svg { width: 11px; height: 11px; fill: var(--orange); flex: none; }

  .person {
    position: absolute; right: 40px; top: 128px; text-align: right;
  }
  .person__name {
    font-size: 21px; font-weight: 700; color: var(--orange); letter-spacing: 1px;
  }
  .person__role { font-size: 13px; color: var(--grey); margin-top: 2px; letter-spacing: 1px; }
  .edge-tab {
    position: absolute; right: 0; top: 138px; width: 18px; height: 36px; background: var(--orange);
  }
  .faint-seal {
    position: absolute; left: 340px; top: 200px; width: 150px; height: 150px;
    border-radius: 50%; border: 5px solid var(--faint); background: rgba(230,230,229,.5);
  }

  .card--back .brand {
    left: 0; right: 0; top: 92px; justify-content: center; font-size: 40px;
  }
  .card--back .brand__mark { width: 20px; height: 20px; }
  .tagline {
    position: absolute; left: 0; right: 0; top: 176px; text-align: center;
    font-size: 15px; font-weight: 500; color: var(--orange);
  }
  .services {
    position: absolute; left: 0; right: 0; top: 202px; text-align: center;
    font-size: 14px; color: var(--grey); letter-spacing: .5px;
  }
</style>
</head>
<body>
  <section class="card card--front">
    <div class="brand"><span class="brand__mark"></span>PELIKAR HIRES</div>
    <p class="address">2210 Harbor Lane, 4th Floor<br>Irvine, CA 92614</p>
    <ul class="contacts">
      <li><svg viewBox="0 0 24 24"><path d="M6.6 10.8a15 15 0 0 0 6.6 6.6l2.2-2.2a1 1 0 0 1 1-.25 11.4 11.4 0 0 0 3.6.57 1 1 0 0 1 1 1V20a1 1 0 0 1-1 1A17 17 0 0 1 3 4a1 1 0 0 1 1-1h3.5a1 1 0 0 1 1 1c0 1.25.2 2.45.57 3.57a1 1 0 0 1-.25 1z"/></svg>555 018-3647</li>
      <li><svg viewBox="0 0 24 24"><path d="M2 5h20v14H2z M2 5l10 8 10-8" /></svg>miles@pelikarhires.com</li>
      <li><svg viewBox="0 0 24 24"><circle cx="12" cy="12" r="10"/></svg>www.pelikarhires.com</li>
    </ul>
    <div class="faint-seal"></div>
    <div class="person">
      <p class="person__name">MILES TANFORD</p>
      <p class="person__role">CEO</p>
    </div>
    <span class="edge-tab"></span>
  </section>

  <section class="card card--back">
    <div class="brand"><span class="brand__mark"></span>PELIKAR HIRES</div>
    <p class="tagline">Luxury Restroom Trailers Rental and Sales</p>
    <p class="services">Weddings | Concerts | Charity | Sporting | Corp</p>
  </section>
</body>
</html>
```